Web Design for New Antenna Company that is ready to revolutionize World Wide Communicaitons

This is the task description that I used for the Logo, please us it as a reference for the “message” of the company.

The name of the Company is "Verdant Arc Incorporated". We build highly efficient antennas that make a direct connection between communication points that make use of highly focus radio beams that support extremely high data rates (wireless internet) over the air.

The reference used for, antenna gain (the measure of an antennas' ability to focus/concentrate energy (radio energy) into a beam is measured by the antennas gain, which uses the Unit vAi, (decibels relative to an isotropic), and these are the initials of our corporate name. Antennas of high gain are focused like a laser, while the reference (isotropic) is a sphere or ball, radiating equally in all directions. The earth is a sphere. Think of Global Communications, as we will offer our products to all parts of the Globe, connecting people with vital information.

I like the feeling of "Direct" as it is definitive, and the idea of the "Beam" in that it carries information, so the main message is contained in the first two words "Verdant Arc" and Incorporated completes the idea and ties to the reference "vAi".

Our tag lines is: "Setting the standard for communications"

I have some 3D antenna patterns (shape of the energy in a 3 dimensional rendering). The colors that are chosen for the rainbow scale are, from most intense to lower intensity, red, sliding through orange to yellow, followed by green and then blue. I also like black for strong contrast. The radiated beam could be outlined in a strong color like black or blue, with a orange/red core color denoting temperature or intense heat (high energy / plasma). My thought of a logo would be a simple but strong image that somehow brings together the descriptions given above, possibly with a intense "beam" as described and possibly in the colors described, as long as the image does not get too "busy" or complex.

Don't feel confined by the use of any particular colors, just use your imagination and see if there is a simple strong image that brings the message home.

Thanks, I appreciate your ideas and look forward to seeing your work.

Regards,

Tam

I have files to share from the previous LOGO design, including EPS files for your use.

Thank you for your interest in providing a website for me.

Also find...

Please find the enclosed links to 3 website that I like, that are in my industry, which is Business to Business in Communications, both Government and Commercial.

Hopefully you can make use of reusing code, so please find something that fits the simple needs that I have.

The first looks too simple for me. The Graphics are too simple, with solid colors, and not too interesting.
http://pwaerials.example/

The second is Kellam Corporation is probably over the top, with the main graphics fanning out to each side. This is a nice effect, but not at all necessary.

I like to top “ribbon” selection” that open into outlined in solid color, filled rounded rectangles. It has a solid look. ( HOME COMPANY MARKETS/SOLUTIONS….)

I like the single page, with information on the bottom of the page, so you do not have to drill down to see what they are about.
http://kellam.example/

The following is probably the closest to what I may really need. This is smaller company, certainly smaller than Kellam, but not so personal as the smallest PW, that includes the designers resume.
http://www.mkfluxon.example/

I like the top of the site to resemble our Business Cards, Letterhead, showing our Logo with full Globe Background, (EPS file) which is enclosed in this mail.

I want to look like a serious company, displaying decades of experience, helping to build our Global Wireless communication system, that we all enjoy today.

I will be writing a Mission Statement, that will be included in the About US, or History Section. I would like to have an area for testimonials, as I have offers from some significant companies that would be happy to provide feedback on our design capabilities.

HOME About US, Markets/Solutions Products/Services

I like that the areas above, when hovered show the pull down without having to actually select the item.

I will enclose, if you send me your e-mail the files to assist... "my favorite" is the Logo, that I like best. I think that the lines and continents on the Globe need to be brought out better so they can be seen. I am including the source files (.eps & .rar)

I will be glad to include other JPEGs of logos that are of different colors on white background. The "tag line" under the name should always be "Setting the Standard for Communications" and not "We set..."

Thanks for your help. I look forward to your proposals Please do not hesitate to call.

Regards,

Tam

Cell # 555-271-9034
tamholt@verdantarcinc.example

I do have files (eps, rar) files for the logo design that I would like used in the website.
Please send an e-mail request at: tamholt@verdantarcinc.example and I will forward them to you.

I can also send you the brief, that was used for the LOGO request, that may provide insight to
the type of message that I want to convey.

Thanks,

Tam

Reason: I am extending to allow enough time so that we are not rushed.

```html
<!DOCTYPE html>
<html lang="en">
<head>
<meta charset="utf-8">
<title>Verdant Arc Incorporated – Welcome</title>
<link rel="stylesheet" href="https://fonts.googleapis.com/css2?family=Maven+Pro:wght@400;500&family=Open+Sans:ital,wght@0,300;0,400;1,300;1,400&display=swap">
<style>
:root{
  --outer:#ebebeb;
  --page:#ffffff;
  --ink:#4a4a4a;
  --muted:#8a8a8a;
  --faint:#b5b5b5;
  --accent:#22bfd8;
  --bar:#3b3d3f;
  --bar-line:#55585b;
  --footer:#33373a;
  --footer-deep:#2a2d2f;
  --footer-text:#6f7a70;
  --footer-head:#c9cdd0;
  --rule:#e6e6e6;
}
*{box-sizing:border-box;margin:0;padding:0}
html,body{width:704px;height:1200px;overflow:hidden}
body{background:var(--outer);font-family:"Maven Pro",Arial,sans-serif;color:var(--ink);position:relative}
.page{position:absolute;left:6px;top:0;width:692px;height:1200px;background:var(--page)}
.block{position:absolute;left:24px;width:656px}

/* brand */
.brand{top:58px;display:flex;align-items:center;justify-content:center;gap:8px}
.brand-dot{width:14px;height:14px;border-radius:50%;background:#1b1b1b}
.brand-name{font-family:"Maven Pro",sans-serif;font-weight:500;font-size:20px;color:#1b1b1b;letter-spacing:.3px}

/* navigation */
.main-nav{top:151px;height:22px;background:var(--bar);border-radius:2px;display:flex;list-style:none}
.main-nav li{display:flex;align-items:center;padding:0 12px;border-right:1px solid var(--bar-line);color:#dcdcdc;font-size:9.5px;gap:4px}
.main-nav li.home{padding:0 13px}
.main-nav .caret{font-size:6px;color:#9a9a9a}

/* hero */
.hero{top:183px;height:232px;background:linear-gradient(180deg,#4f4a40 0%,#8c8674 28%,#a59e88 45%,#6f6550 66%,#8a7a48 82%,#5a4a2c 100%)}
.hero-base{top:415px;height:2px;background:#c9b670}
.divider{top:427px;height:4px;background:repeating-linear-gradient(135deg,var(--rule) 0 1px,transparent 1px 3px)}

/* welcome */
.welcome{top:448px;text-align:center}
.welcome h1{font-family:"Open Sans",sans-serif;font-weight:300;font-size:19px;color:#555}
.welcome h1 .accent{color:var(--accent)}
.welcome p{margin:3px auto 0;width:640px;font-family:"Open Sans",sans-serif;font-style:italic;font-weight:300;font-size:12.6px;line-height:16px;color:var(--faint)}
.actions{top:533px;display:flex;justify-content:center;gap:6px}
.btn{height:19px;padding:0 10px;font-size:10px;line-height:19px;color:#fff;border-radius:2px}
.btn-dark{background:var(--bar)}
.btn-accent{background:var(--accent)}

/* section titles */
.section-title{display:flex;align-items:center;gap:6px;font-family:"Open Sans",sans-serif;font-size:12px;color:#555}
.section-title::after{content:"";flex:1;height:6px;background:repeating-linear-gradient(135deg,var(--rule) 0 1px,transparent 1px 3px)}

.about{top:585px}
.about p{margin-top:8px;font-size:7.6px;line-height:12.3px;color:#666}

/* antennas tabs */
.antennas{top:790px;left:24px;width:322px}
.tabs{display:flex;gap:3px;margin-top:11px;list-style:none}
.tabs li{font-size:7.5px;color:#777;padding:4px 8px;border:1px solid #e1e1e1;border-bottom:none;background:#f6f6f6}
.tabs li.active{background:#fff;color:#555}
.tab-panel{height:193px;border:1px solid #e6e6e6;position:relative}
.diagram{position:absolute;left:18px;top:17px;width:280px;height:150px;background:linear-gradient(180deg,#a9a9a9 0 14px,#f1f1f1 14px);border:2px solid #bdbdbd}

/* testimonials */
.testimonials{top:790px;left:360px;width:320px}
.testimonials .section-title{padding-right:34px;position:relative}
.arrows{position:absolute;right:0;top:2px;display:flex;gap:3px}
.arrows span{width:11px;height:11px;border-radius:50%;background:#b8b8b8}
.arrows span+span{background:#7d7d7d}
.quote{margin-top:11px;border:1px solid #e3e3e3;background:#f8f8f8;padding:8px 10px 8px 32px;position:relative;font-family:"Open Sans",sans-serif;font-style:italic;font-size:7px;line-height:12px;color:#999}
.quote::before{content:"\201C";position:absolute;left:10px;top:2px;font-size:18px;color:#c2c2c2;font-style:normal}
.author{margin:6px 0 0 32px;font-size:9px;color:#555;display:flex;align-items:center;gap:6px}
.role{margin-left:32px;font-size:6.5px;color:#b0b0b0}

/* footer */
.site-footer{position:absolute;left:0;top:1048px;width:692px;height:125px;background:var(--footer)}
.f-col{position:absolute;top:19px}
.f-col h4{font-weight:400;font-size:9.5px;color:var(--footer-head);margin-bottom:11px}
.f-about{left:18px;width:160px;font-size:7.3px;line-height:12.2px;color:var(--footer-text)}
.f-nav{left:198px;list-style:none}
.f-nav li{font-size:7.3px;line-height:12.6px;color:var(--footer-text)}
.f-nav li::before{content:"›";margin-right:6px}
.f-news{left:354px;width:150px}
.news{display:flex;gap:10px;margin-bottom:8px}
.thumb{width:30px;height:24px;flex:none;border:2px solid #e8e8e8}
.news p{font-size:7px;line-height:9px;color:var(--footer-text)}
.news small{display:block;margin-top:4px;font-size:6px;color:#5d655e}
.f-contact{left:521px;list-style:none}
.f-contact li{display:flex;align-items:center;gap:10px;font-size:7.3px;line-height:17px;color:var(--footer-text)}
.f-contact svg{width:8px;height:8px;fill:#a6acae}
.f-contact h4{margin-bottom:5px}
.bottom-bar{position:absolute;left:0;top:1173px;width:692px;height:27px;background:var(--footer-deep);display:flex;align-items:center;justify-content:space-between;padding:0 18px}
.bottom-bar p{font-size:6.8px;color:#7c8484}
.social{display:flex;gap:10px}
.social span{width:14px;height:14px;border-radius:50%;background:#6e7476}
</style>
</head>
<body>
<div class="page">

  <div class="block brand">
    <span class="brand-dot"></span>
    <span class="brand-name">Verdant Arc Incorporated</span>
  </div>

  <ul class="block main-nav">
    <li class="home"><svg width="8" height="8" viewBox="0 0 10 10"><path d="M5 1 1 5h1.5v4h2V6.5h1V9h2V5H9z" fill="#e0e0e0"/></svg></li>
    <li>Home <span class="caret">▼</span></li>
    <li>Page Templates <span class="caret">▼</span></li>
    <li>Features <span class="caret">▼</span></li>
    <li>Portfolio <span class="caret">▼</span></li>
    <li>Our Blog <span class="caret">▼</span></li>
    <li>Contact Us</li>
  </ul>

  <div class="block hero" role="img" aria-label="Large radio telescope dish on a steel frame under a dramatic cloudy sky"></div>
  <div class="block hero-base"></div>
  <div class="block divider"></div>

  <section class="block welcome">
    <h1><span class="accent">VERDANT ARC INCORPORATED</span>- Welcome To Our Website</h1>
    <p>We build highly efficient antennas that make a direct connection between communication points that make use of highly focus radio beams that support extremely high data rates (wireless internet) over the air.</p>
  </section>
  <div class="block actions">
    <span class="btn btn-dark">Projects</span>
    <span class="btn btn-accent">Our Services</span>
  </div>

  <section class="block about">
    <h2 class="section-title">About Us</h2>
    <p>Lorem ipsum dolor sit amet, consectetur adipiscing elit. Quisque hendrerit turpis quis nisl rhoncus ac venenatis odio tempor. Maecenas adipiscing nisl sit amet lectus laoreet interdum. Sed non elit quis eros blandit auctor in in dolor. Donec malesuada aliquam eros non tincidunt. Nam cursus lobortis enim. Etiam non faucibus lorem. Donec tincidunt velit posuere ante vehicula nec mattis justo hendrerit. Duis id sapien eget velit tincidunt egestas. Sed ac accumsan lorem.Lorem ipsum dolor sit amet, consectetur adipiscing elit. Quisque hendrerit turpis quis nisl rhoncus ac venenatis odio tempor. Maecenas adipiscing nisl sit amet lectus laoreet interdum. Sed non elit quis eros blandit auctor in in dolor. Donec malesuada aliquam eros non tincidunt. Nam cursus lobortis enim. Etiam non faucibus lorem. Donec tincidunt velit posuere ante vehicula nec mattis justo hendrerit. Duis id sapien eget velit tincidunt egestas. Sed ac accumsan lorem. Lorem ipsum dolor sit amet, consectetur adipiscing elit. Quisque hendrerit turpis quis nisl rhoncus ac venenatis odio tempor. Maecenas adipiscing nisl sit amet lectus laoreet interdum. Sed non elit quis eros blandit auctor in in dolor. Donec malesuada aliquam eros non tincidunt. Nam cursus lobortis enim. Etiam non faucibus lorem. Donec tincidunt velit posuere ante vehicula nec mattis justo hendrerit. Duis id sapien eget velit tincidunt egestas. Sed ac accumsan lorem.</p>
  </section>

  <section class="block antennas">
    <h2 class="section-title">Type of Antennas</h2>
    <ul class="tabs">
      <li class="active">Parabolic Antenna</li>
      <li>Features</li>
      <li>Radiation Pattern</li>
    </ul>
    <div class="tab-panel">
      <div class="diagram" role="img" aria-label="Technical diagram of typical parabolic antennas with side and down view radiation emission patterns"></div>
    </div>
  </section>

  <section class="block testimonials">
    <h2 class="section-title">Client Testimonials<span class="arrows"><span></span><span></span></span></h2>
    <blockquote class="quote">Wow, just the template we were looking for! Stunning clean design, element rich, clean code, browser friendly and easy to manage. Keep up the good work GreyFinchStudio!</blockquote>
    <p class="author"><svg width="8" height="8" viewBox="0 0 10 10"><circle cx="5" cy="3" r="2.2" fill="#666"/><path d="M1 10c0-3 2-4.5 4-4.5S9 7 9 10z" fill="#666"/></svg>Owen Marsh</p>
    <p class="role">Developer, Kestrel</p>
  </section>

  <footer class="site-footer">
    <div class="f-col f-about">
      <h4>About Us</h4>
      Twenty years from now you will be more disappointed by the things that you didn't do than by the ones you did do. So throw off the bowlines. Sail away from the safe harbor. Catch the trade winds. Explore. Dream. Discover.
    </div>
    <ul class="f-col f-nav">
      <h4>Footer Navigation</h4>
      <li>Home</li><li>Our Services</li><li>Recent Work</li><li>Our Blog</li><li>About Us</li><li>Contact Us</li>
    </ul>
    <div class="f-col f-news">
      <h4>Latest News</h4>
      <div class="news"><span class="thumb" role="img" aria-label="News thumbnail photo" style="background:linear-gradient(135deg,#d8d2c8,#9aa4a8)"></span><p>Those who mind don't matter, and vice-versa.<small>8 Sept., 2012</small></p></div>
      <div class="news"><span class="thumb" role="img" aria-label="News thumbnail photo" style="background:linear-gradient(135deg,#cfd9de,#b8a99a)"></span><p>Be yourself; everyone else is already taken.<small>2 Sept., 2012</small></p></div>
    </div>
    <ul class="f-col f-contact">
      <h4>Get In Touch with Us</h4>
      <li><svg viewBox="0 0 10 10"><rect x="2.5" y="0.5" width="5" height="9" rx="1"/></svg>(555) 014 2290</li>
      <li><svg viewBox="0 0 10 10"><path d="M0 2h10v6H0z"/><path d="M0 2l5 3.5L10 2" stroke="#33373a" fill="none"/></svg>contact@verdantarc.example</li>
      <li><svg viewBox="0 0 10 10"><path d="M5 0a3.5 3.5 0 0 0-3.5 3.5C1.5 6 5 10 5 10s3.5-4 3.5-6.5A3.5 3.5 0 0 0 5 0zm0 5a1.4 1.4 0 1 1 0-2.8A1.4 1.4 0 0 1 5 5z"/></svg>1820 Orchard Ave., Lakeport City</li>
    </ul>
  </footer>
  <div class="bottom-bar">
    <p>Verdant Arc Incorporated © 2013</p>
    <div class="social"><span></span><span></span><span></span><span></span><span></span></div>
  </div>

</div>
</body>
</html>
```